Postcard Design/Coupon

My business is a Pizza Shop/Restaurant/Bar. I know confusing. I sell mainly pizza and beer but sandwich's and salads are a big seller also. So I want coupons/postcards that I can hand out to every table that comes in to entice them to come back. I also will be sending these coupons/postcards to delivery customers. The business name is Larkdale Pizza Vento address is 581 Thistle Avenue Sewickley PA15077 phone number is 412-741-1744On one side I wanted the coupon offer and logo and the other side the hours but also room for me to send some out.

Target Market(s)

Families

Industry/Entity Type

Restaurant

Requirements
Must have
• Pizza
Nice to have
• Salads/Hoagies/Nice Description

```html
<!DOCTYPE html>
<html lang="en">
<head>
<meta charset="utf-8">
<title>Larkdale Pizza Vento – Postcard</title>
<link rel="stylesheet" href="https://fonts.googleapis.com/css2?family=Cinzel:wght@700&family=Oswald:wght@500;700&family=PT+Sans+Narrow:wght@400;700&family=Kalam:wght@400&family=Open+Sans:wght@400;700;800&display=swap">
<style>
:root{
  --backdrop:#4a3527;
  --olive-light:#c7cd6e;
  --olive-dark:#a9b24a;
  --ink:#111;
  --white:#fff;
  --red:#cf2534;
  --green:#1f9446;
  --panel:rgba(190,214,110,.78);
  --crust:#d9a25a;
  --cheese:#efd27a;
  --sauce:#b7412c;
  --leaf:#7fae3e;
}
*{box-sizing:border-box;margin:0;padding:0}
html,body{width:1200px;height:500px;overflow:hidden;background:var(--backdrop)}
.canvas{position:relative;width:1200px;height:500px}
.card{position:absolute;top:37px;height:430px;overflow:hidden}
.card--front{left:22px;width:563px;background:linear-gradient(160deg,var(--olive-light),var(--olive-dark))}
.card--back{left:605px;width:560px;background:#000}
.logo-name{font-family:"Cinzel",serif;font-weight:700;color:var(--ink);line-height:1.05;text-align:center}
.address{font-family:"Cinzel",serif;font-weight:700;font-size:11.5px;color:var(--ink);text-align:center;white-space:nowrap}
.front-logo{position:absolute;left:14px;top:40px;width:260px}
.front-logo .logo-name{font-size:32px}
.front-logo .address{margin-top:8px}
.coupon{position:absolute;left:285px;top:23px;width:251px;height:98px;background:var(--white);border:2px dashed #999;border-radius:8px;display:flex;align-items:center;padding:6px 8px;gap:6px}
.coupon .logo-name{font-size:10px;width:64px;flex:none}
.coupon-offer{text-align:center;flex:1}
.coupon-offer h2{font-family:"Oswald",sans-serif;font-weight:700;font-size:27px;color:var(--red);line-height:1.1;white-space:nowrap}
.coupon-offer p{font-family:"PT Sans Narrow",sans-serif;font-size:14px;color:var(--ink);line-height:1.25;margin-top:4px}
.photo{position:absolute}
.photo--pizza-slice{left:0;top:130px;width:370px;height:124px;border-radius:0 60px 0 0;background:radial-gradient(ellipse at 45% 55%,var(--cheese),var(--sauce) 55%,var(--crust) 80%,transparent 82%)}
.about{position:absolute;left:376px;top:142px;width:182px;font-family:"PT Sans Narrow",sans-serif;font-size:12.5px;line-height:1.3;color:var(--ink)}
.delivery-band{position:absolute;left:0;top:254px;width:563px;height:38px;background:var(--ink);display:flex;align-items:center;justify-content:center;gap:26px;color:var(--white)}
.delivery-band .label{font-family:"Kalam",cursive;font-size:21px}
.phone{display:flex;align-items:center;gap:6px;font-family:"Open Sans",sans-serif;font-weight:800;letter-spacing:.5px}
.delivery-band .phone{font-size:21px}
.photo--salad,.photo--hoagie{border:4px solid var(--white);border-radius:50%}
.photo--salad{left:24px;top:300px;width:112px;height:112px;background:radial-gradient(circle,var(--leaf),#3f6b2a 70%)}
.photo--hoagie{left:162px;top:296px;width:118px;height:118px;background:radial-gradient(circle,#c0392b 20%,#e8c38a 50%,#b98448 80%)}
.promo{position:absolute;left:306px;width:257px;height:55px;border-radius:12px 0 0 12px;color:var(--white);font-family:"Open Sans",sans-serif;font-weight:400;font-size:12.5px;line-height:1.3;padding:6px 30px 0 24px}
.promo--salad{top:303px;background:var(--green)}
.promo--hoagie{top:368px;background:var(--red)}
.tagline-band{position:absolute;left:0;top:0;width:560px;height:36px;background:#000;color:var(--white);font-family:"Open Sans",sans-serif;font-weight:800;font-size:20px;letter-spacing:1.5px;display:flex;align-items:center;justify-content:center}
.photo--pizza-whole{left:0;top:36px;width:560px;height:394px;background:radial-gradient(ellipse at 30% 60%,#d8d290,#b5a85b 45%,#8a5a2c 75%,#4d2e1a)}
.info-panel{position:absolute;left:12px;top:63px;width:277px;height:322px;background:var(--panel)}
.info-panel .logo-name{margin-top:20px;font-size:31px}
.info-panel .address{margin-top:6px}
.phone-band{margin-top:10px;height:27px;background:var(--red);color:var(--white);display:flex;align-items:center;padding-left:40px}
.phone-band .phone{font-size:20px}
.hours{margin-top:14px;text-align:center;font-family:"Cinzel",serif;font-weight:700;color:#222}
.hours h3{font-size:17px;margin-bottom:8px}
.hours p{font-size:13px;line-height:1.45}
.closed-pill{display:inline-block;margin-top:7px;padding:2px 10px;background:var(--green);color:var(--white);border:2px solid var(--white);border-radius:9px;font-size:14px}
.mail-area{position:absolute;left:300px;top:81px;width:260px;height:349px;background:var(--white)}
.stamp-box{position:absolute;right:13px;top:8px;width:55px;height:52px;border:1.5px dashed #aaa}
</style>
</head>
<body>
<main class="canvas">
  <section class="card card--front" aria-label="Coupon side">
    <div class="front-logo">
      <div class="logo-name">Larkdale Pizza Vento</div>
      <div class="address">581 Thistle Avenue, Larkdale PA15077</div>
    </div>
    <div class="coupon">
      <div class="logo-name">Larkdale Pizza Vento</div>
      <div class="coupon-offer">
        <h2>$5 OFF PIZZA</h2>
        <p>with purchase of any<br>large or extra large Pizza</p>
      </div>
    </div>
    <div class="photo photo--pizza-slice" role="img" aria-label="Photo of a pepperoni, olive and mushroom pizza with a slice being lifted"></div>
    <p class="about">Larkdale Pizza Vento is a family owned business committed to satisfying our customers. We take pride in creating the best pizza in Larkdale. Both the dough and the sauce are made from our own recipe in our own shop.</p>
    <div class="delivery-band">
      <span class="label">Home Delivery</span>
      <span class="phone">
        <svg width="20" height="20" viewBox="0 0 20 20" aria-hidden="true"><circle cx="10" cy="10" r="9" fill="none" stroke="#fff" stroke-width="1.5"/><path d="M7 5c-1 1-1.5 3 0 6s4 4.5 5.5 4l1-1.5-2-1.5-1 .8c-1-.5-2-2-2.3-3l.9-.8-1-2.2z" fill="#fff"/></svg>
        412.555.0187
      </span>
    </div>
    <div class="photo photo--salad" role="img" aria-label="Photo of a fresh garden salad"></div>
    <div class="photo photo--hoagie" role="img" aria-label="Photo of a hoagie sandwich"></div>
    <p class="promo promo--salad">Taste our sumptuous salad made with the freshest ingredients available.</p>
    <p class="promo promo--hoagie">Try one of our delicious hoagies made to your own specifications.</p>
  </section>

  <section class="card card--back" aria-label="Hours and mailing side">
    <div class="tagline-band">GREAT PIZZA, SALADS, HOAGIES, BEER</div>
    <div class="photo photo--pizza-whole" role="img" aria-label="Close-up photo of a baked pizza"></div>
    <div class="info-panel">
      <div class="logo-name">Larkdale Pizza Vento</div>
      <div class="address">581 Thistle Avenue, Larkdale PA15077</div>
      <div class="phone-band">
        <span class="phone">
          <svg width="20" height="20" viewBox="0 0 20 20" aria-hidden="true"><circle cx="10" cy="10" r="9" fill="none" stroke="#fff" stroke-width="1.5"/><path d="M7 5c-1 1-1.5 3 0 6s4 4.5 5.5 4l1-1.5-2-1.5-1 .8c-1-.5-2-2-2.3-3l.9-.8-1-2.2z" fill="#fff"/></svg>
          412.555.0187
        </span>
      </div>
      <div class="hours">
        <h3>STORE HOURS</h3>
        <p>Monday to Friday<br>11 AM to 10 PM<br>Saturday<br>11 AM to 11 PM</p>
        <span class="closed-pill">SUNDAY CLOSED</span>
      </div>
    </div>
    <div class="mail-area"><div class="stamp-box"></div></div>
  </section>
</main>
</body>
</html>
```